Tallow Brook Ranch all natural beef packaging

I would like a custom label to affix to my packages of steaks, roasts, and burgers. The packaging label should be simple and represent the all natural, healthy and humane way we raise our grass finished and natural grain finished beef. check out www.tallowbrookranch.example for photos of the ranch and information about our cattle.

Target Market(s)

consumers who wish to purchase beef that is born and raised in Ohio, never given any antibiotics, implants, or hormones. Cattle are never confined, always on pasture, even when finished on grain. Humane treatment of the animals which are handled by horseback and on foot.

Industry/Entity Type

Ranch

Requirements
Must have
• Must be able to incorporate the National Pastureland Society label.
• http://www.nationalpastureland.example/
• I like dark colors, rich and earthy, but maybe on a white background to stand out on the clear plastic wrap over the beef. Imagine you're buying a steak at Parlows and look at how the packaging stands off from the color of the meat.
Nice to have
• I would like a very simple label that incorporates some icon or picture of a calf or cow. See my website www.tallowbrookranch.example

```html
<!DOCTYPE html>
<html lang="en">
<head>
<meta charset="utf-8">
<title>Tallow Brook Ranch – Beef Label</title>
<link href="https://fonts.googleapis.com/css2?family=Great+Vibes&family=Oswald:wght@500;700&family=Roboto+Condensed:ital,wght@0,400;0,700;1,400&display=swap" rel="stylesheet">
<style>
  :root {
    --ranch-green: #2f6b3a;
    --ranch-green-light: #5c8f4a;
    --beef-red: #c0272d;
    --label-white: #ffffff;
    --label-rim: #9a9a9a;
    --backdrop: #ececec;
    --ink-grey: #4a4a4a;
  }
  * { margin: 0; padding: 0; box-sizing: border-box; }
  html, body { width: 889px; height: 1200px; overflow: hidden; }
  body {
    background: var(--backdrop);
    display: flex; align-items: center; justify-content: center;
    font-family: "Roboto Condensed", Arial, sans-serif;
  }
  .label {
    position: relative;
    width: 820px; height: 470px;
    border-radius: 50%;
    background: var(--label-white);
    border: 6px solid var(--label-rim);
    box-shadow: 0 0 0 3px var(--label-white), 0 0 0 5px #cfcfcf;
    overflow: hidden;
  }
  .ranch-name {
    position: absolute; top: 26px; left: 0; width: 100%;
    text-align: center;
    font-family: "Great Vibes", cursive;
    font-size: 60px; color: var(--ranch-green);
    line-height: 1;
  }
  .pasture-scene {
    position: absolute; top: 100px; left: 150px;
    width: 520px; height: 84px;
    background: linear-gradient(180deg, rgba(47,107,58,0) 0%, rgba(47,107,58,0.25) 40%, var(--ranch-green) 100%);
    border-radius: 40px 40px 0 0;
  }
  .cert-badge {
    position: absolute; top: 120px; left: 92px;
    width: 76px; height: 76px; border-radius: 50%;
    background: var(--ranch-green-light);
    border: 3px solid var(--ranch-green);
  }
  .ohio-mark {
    position: absolute; top: 98px; left: 648px;
    width: 66px; height: 78px;
    background: var(--beef-red);
    border-radius: 6px 14px 10px 18px;
  }
  .ohio-note {
    position: absolute; top: 112px; left: 656px; width: 52px;
    font-size: 9px; line-height: 1.15; color: var(--label-white);
    font-weight: 700; text-align: center; text-transform: uppercase;
  }
  .horizon {
    position: absolute; top: 190px; left: 150px; width: 520px; height: 4px;
    background: var(--ranch-green);
  }
  .claims {
    position: absolute; top: 212px; left: 80px; width: 130px;
    font-size: 11px; line-height: 1.25; font-weight: 700;
    color: var(--beef-red); text-transform: uppercase;
  }
  .net-weight {
    position: absolute; top: 222px; left: 620px;
    font-size: 12px; font-weight: 700; color: var(--ink-grey);
    display: flex; align-items: center; gap: 6px;
  }
  .net-weight .box {
    width: 64px; height: 20px; border: 1.5px solid var(--ink-grey);
    border-radius: 3px;
  }
  .grade {
    position: absolute; top: 200px; left: 0; width: 100%; text-align: center;
    font-family: "Oswald", "Arial Narrow", sans-serif;
  }
  .grade .tagline {
    font-size: 27px; font-weight: 700; color: var(--ranch-green);
    letter-spacing: 0.5px; line-height: 1.1;
  }
  .grade .breed {
    font-size: 68px; font-weight: 700; color: var(--beef-red);
    line-height: 1.05; letter-spacing: 1px;
  }
  .natural-line {
    position: absolute; top: 312px; left: 0; width: 100%;
    display: flex; align-items: center; justify-content: center; gap: 12px;
    font-size: 12px; font-weight: 700; color: var(--ranch-green);
    text-transform: uppercase;
  }
  .natural-line .bar { width: 130px; height: 10px; background: var(--ranch-green); }
  .origin {
    position: absolute; top: 344px; left: 0; width: 100%; text-align: center;
    font-size: 19px; color: var(--ranch-green); letter-spacing: 0.5px;
  }
  .promise {
    position: absolute; top: 394px; left: 0; width: 100%; text-align: center;
    font-size: 13px; font-style: italic; color: var(--ranch-green);
  }
</style>
</head>
<body>
  <div class="label">
    <div class="ranch-name">Tallow Brook Ranch</div>
    <div class="pasture-scene" role="img" aria-label="Green silhouette of cattle and a rancher standing on pasture grass"></div>
    <div class="cert-badge" role="img" aria-label="National Pastureland Society certification badge"></div>
    <div class="ohio-mark" role="img" aria-label="Red outline of the state of Ohio"></div>
    <div class="ohio-note">Born and raised in Ohio</div>
    <div class="horizon"></div>
    <div class="claims">No antibiotics, no added hormones, no implants</div>
    <div class="net-weight">NET WT. <span class="box"></span> OZ</div>
    <div class="grade">
      <div class="tagline">100% GRASSFED BEEF</div>
      <div class="breed">ANGUS BEEF</div>
    </div>
    <div class="natural-line"><span class="bar"></span>All natural to our cattle<span class="bar"></span></div>
    <div class="origin">PRODUCT OF USA</div>
    <div class="promise">Pasture raised, humanely handled, always on open grass.</div>
  </div>
</body>
</html>
```